Tallowbrook Aesthetic Medic is the title and the name of the business

Chatterleaf advertising: keep
To those dimensions

Aimed at Caucasian women between the ages of 18 - 60 interested in beauty and cosmetic injectables. Will be boosted on chatterleaf which is my advertising platform.

Name: Tallowbrook Aesthetic Medic
0491 570 318

Forehead $58
Frown lines $116
Crows feet $116
Lip fillers $380

I would like to have a beautiful girl that suits the picture.

Target Market(s)

Females between 18 - 60 interested in Lumiset and cosmetic fillers
Prefer Caucasian as that's the majority of population

Industry/Entity Type

Beauty Salon

Font styles to use
Serif
Script

Colors
e667a6
eea4c8
f9d9e8
fee18a
fbf289
fbee3d
cadf82
cedeed
85cae6

Requirements
Must have
• Name: Tallowbrook Aesthetic Medic
• Phone number: 0491 570 381
• Prices:
• Forehead $58
• Frown lines $116
• Crows feet $116
• Lip fillers $380
• Picture of female that is very beautiful
Nice to have
• Not a cartoon or anything else that's not a real picture of a female
Should not have
• No cartoon pictures. Proper picture of women

```html
<!DOCTYPE html>
<html lang="en">
<head>
<meta charset="utf-8">
<title>Tallowbrook Aesthetic Medic – Injectables Price List</title>
<link rel="stylesheet" href="https://fonts.googleapis.com/css2?family=Marcellus&family=Exo+2:wght@700&family=Arimo:wght@400&family=Passion+One:wght@400&display=swap">
<style>
  :root {
    --bg-dark: #5f6064;
    --bg-mid: #9a9b9f;
    --bg-light: #d6d6d8;
    --title: #7a2c46;
    --title-edge: #f1d9df;
    --ink-dark: #3a1631;
    --panel: #2e1429;
    --frame: #ffffff;
    --label: #efc3ab;
    --price: #d84e5c;
    --hair-dark: #3b2618;
    --hair-mid: #6e4a30;
    --skin: #e8c4aa;
  }
  * { margin: 0; padding: 0; box-sizing: border-box; }
  html, body { width: 1200px; height: 628px; overflow: hidden; }
  body { background: var(--bg-light); }

  .ad {
    position: relative;
    width: 1200px;
    height: 628px;
    overflow: hidden;
    background: linear-gradient(100deg, var(--bg-dark) 0%, var(--bg-mid) 30%, var(--bg-light) 55%, var(--bg-mid) 100%);
  }

  .model-photo {
    position: absolute;
    left: 470px;
    top: 0;
    width: 730px;
    height: 628px;
    background:
      radial-gradient(ellipse 230px 300px at 460px 300px, var(--skin) 0%, var(--skin) 55%, rgba(232,196,170,0) 100%),
      linear-gradient(90deg, rgba(59,38,24,0) 0%, var(--hair-mid) 30%, var(--hair-dark) 55%, var(--hair-mid) 85%, var(--hair-dark) 100%);
    -webkit-mask-image: linear-gradient(90deg, transparent 0%, #000 22%);
            mask-image: linear-gradient(90deg, transparent 0%, #000 22%);
  }

  .business-name {
    position: absolute;
    left: 38px;
    top: 38px;
    font-family: "Marcellus", serif;
    color: var(--title);
    letter-spacing: 3px;
    line-height: 1;
    text-shadow: 1px 1px 0 var(--title-edge), -1px -1px 0 rgba(255,255,255,0.35);
  }
  .business-name .line-one { display: block; font-size: 56px; }
  .business-name .line-two { display: block; font-size: 47px; margin-top: 16px; }

  .phone {
    position: absolute;
    left: 38px;
    top: 208px;
    display: flex;
    align-items: center;
    gap: 8px;
    font-family: "Exo 2", sans-serif;
    font-weight: 700;
    font-size: 28px;
    letter-spacing: 1px;
    color: var(--ink-dark);
  }
  .phone-icon { width: 54px; height: 54px; }

  .price-board {
    position: absolute;
    left: 33px;
    top: 302px;
    width: 815px;
    height: 290px;
    background: var(--frame);
    padding: 6px 4px;
    display: flex;
    gap: 3px;
  }
  .price-item {
    flex: 1;
    background: var(--panel);
    display: flex;
    flex-direction: column;
    align-items: center;
    text-align: center;
    padding-top: 28px;
  }
  .treatment {
    font-family: "Arimo", sans-serif;
    font-size: 40px;
    line-height: 1.2;
    color: var(--label);
    height: 110px;
  }
  .amount {
    margin-top: 22px;
    font-family: "Passion One", sans-serif;
    font-size: 70px;
    line-height: 1;
    color: var(--price);
  }
</style>
</head>
<body>
  <main class="ad">
    <div class="model-photo" role="img" aria-label="Photograph of a beautiful woman with long flowing brown hair and glossy pink lips, looking at the viewer"></div>

    <h1 class="business-name">
      <span class="line-one">Tallowbrook</span>
      <span class="line-two">Aesthetic Medic</span>
    </h1>

    <p class="phone">
      <svg class="phone-icon" viewBox="0 0 54 54" aria-hidden="true">
        <circle cx="27" cy="27" r="23" fill="none" stroke="var(--ink-dark)" stroke-width="4"/>
        <path d="M19 15c2-1 4 0 5 2l2 4c1 2 0 3-1 4l-1 1c1 3 4 6 7 7l1-1c1-1 2-2 4-1l4 2c2 1 3 3 2 5l-1 2c-1 2-3 3-6 2-8-2-16-10-18-18-1-3 0-5 2-6z" fill="var(--ink-dark)"/>
      </svg>
      <span class="phone-number">0491.570.381</span>
    </p>

    <section class="price-board" aria-label="Treatment prices">
      <div class="price-item">
        <div class="treatment">Fore-<br>head</div>
        <div class="amount">$58</div>
      </div>
      <div class="price-item">
        <div class="treatment">Frown<br>Lines</div>
        <div class="amount">$116</div>
      </div>
      <div class="price-item">
        <div class="treatment">Crows<br>Feet</div>
        <div class="amount">$116</div>
      </div>
      <div class="price-item">
        <div class="treatment">Lip<br>Fillers</div>
        <div class="amount">$380</div>
      </div>
    </section>
  </main>
</body>
</html>
```